We need a brochure designed for each of our 4 online training schools. All content will be supplied and most of the graphics. We have just had our websites rebranded and brochure needs to reflect the same design/brand....so we have a very clear design look for you to follow. Each brochure version will have very similar content...just different logos, links and images.

Brochure needs to have a click through table of contents and links to website within it. Example of brochure attached. We need the first of these asap....but we will need 3 more versions based on exactly the same layout over the coming 2 weeks.

Payment is now for one editable version of brochure.  With both working and finished file to be sent to us.

Industry/Entity Type

Training

```html
<!DOCTYPE html>
<html lang="en">
<head>
<meta charset="utf-8">
<title>Courses – Harbour School of Events</title>
<link href="https://fonts.googleapis.com/css2?family=PT+Sans:ital,wght@0,400;0,700;1,400&display=swap" rel="stylesheet">
<style>
  :root {
    --salmon: #f3876d;
    --salmon-deep: #ec7a60;
    --ink: #2b1710;
    --panel: rgba(12, 10, 10, 0.74);
    --button: #151111;
    --white: #ffffff;
    --divider: rgba(255, 255, 255, 0.85);
  }
  * { box-sizing: border-box; margin: 0; padding: 0; }
  html, body { width: 1200px; height: 848px; overflow: hidden; }
  body { font-family: "PT Sans", Arial, sans-serif; background: #d9d3c6; }

  .page { position: relative; width: 1200px; height: 848px; overflow: hidden; }

  .backdrop {
    position: absolute; inset: 0;
    background:
      radial-gradient(ellipse 220px 160px at 560px 110px, rgba(244, 196, 196, 0.9), transparent 70%),
      radial-gradient(ellipse 200px 170px at 980px 160px, rgba(240, 218, 214, 0.9), transparent 70%),
      radial-gradient(ellipse 220px 200px at 150px 140px, rgba(238, 214, 204, 0.9), transparent 70%),
      radial-gradient(ellipse 240px 200px at 1130px 420px, rgba(233, 232, 206, 0.9), transparent 70%),
      radial-gradient(ellipse 260px 220px at 60px 520px, rgba(200, 180, 150, 0.8), transparent 70%),
      radial-gradient(ellipse 300px 200px at 620px 760px, rgba(232, 220, 206, 0.9), transparent 70%),
      linear-gradient(180deg, #b7b79a 0%, #cfc6b2 45%, #d8cfc2 100%);
  }

  .brand {
    position: absolute; top: 8px; left: 561px;
    display: flex; align-items: center; gap: 8px;
  }
  .brand-name {
    background: #f4f1ee; color: var(--ink);
    width: 44px; height: 36px; padding: 3px;
    font-size: 7px; line-height: 8px; font-weight: 700;
    text-align: center; display: flex; align-items: center; justify-content: center;
  }
  .page-number {
    color: #5a4a44; font-size: 13px;
    border-left: 1px solid #7a6a64; padding-left: 6px; line-height: 16px;
  }

  .page-title {
    position: absolute; top: 64px; left: 0; width: 100%;
    text-align: center; color: var(--white);
    font-size: 39px; font-weight: 400; letter-spacing: 0.5px;
  }

  .divider {
    position: absolute; top: 190px; width: 1.5px; height: 552px;
    background: var(--divider);
  }

  .course { position: absolute; top: 139px; width: 310px; }
  .course-icon { display: block; width: 78px; height: 46px; margin: 0 auto 15px; }
  .course-title {
    background: var(--salmon); color: var(--ink);
    height: 57px; padding: 4px 12px 0;
    font-size: 21px; line-height: 25px; font-weight: 700; text-transform: uppercase;
  }
  .course-price {
    margin-top: 9px; height: 28px;
    background: var(--salmon); color: var(--white);
    font-style: italic; font-size: 20px; line-height: 28px; padding-left: 10px;
  }
  .course-body {
    margin-top: 10px; height: 438px; position: relative;
    background: var(--panel);
    padding: 22px 18px 0 15px;
    color: var(--white); font-size: 13.4px; line-height: 19px;
  }
  .course-actions {
    position: absolute; left: 0; right: 0; bottom: 0; height: 48px;
    background: var(--salmon-deep);
    display: flex; align-items: center; justify-content: space-between; padding: 0 6px;
  }
  .course-actions a {
    display: block; width: 92px; height: 36px; background: var(--button);
    color: #f7dcd4; text-decoration: none; font-size: 16px; line-height: 36px; text-align: center;
  }

  .contact-bar {
    position: absolute; left: 0; bottom: 0; width: 1200px; height: 77px;
    background: var(--salmon);
  }
  .contact-item {
    position: absolute; top: 14px; width: 200px; margin-left: -100px;
    text-align: center; color: var(--white); font-size: 13px;
  }
  .contact-item svg { display: block; width: 17px; height: 17px; margin: 0 auto 8px; }
</style>
</head>
<body>
<main class="page">
  <div class="backdrop" role="img" aria-label="Soft-focus photograph of pink, peach and white wedding flowers with green foliage"></div>

  <header class="brand">
    <div class="brand-name">Harbour School of Events</div>
    <span class="page-number">03</span>
  </header>

  <h1 class="page-title">COURSES</h1>

  <span class="divider" style="left:421px"></span>
  <span class="divider" style="left:775px"></span>

  <article class="course" style="left:90px">
    <svg class="course-icon" viewBox="0 0 78 46" aria-hidden="true"><polygon points="39,2 76,16 39,30 2,16" fill="#1a1412"/><path d="M18 22 v14 c10 8 32 8 42 0 v-14 l-21 8z" fill="#1a1412"/><path d="M68 19 v16" stroke="#1a1412" stroke-width="2"/><rect x="65.5" y="34" width="5" height="9" fill="#1a1412"/></svg>
    <h2 class="course-title">Certificate in<br>Wedding Planning</h2>
    <p class="course-price">Get started for as little as £70</p>
    <div class="course-body">
      <p>The Certificate in Wedding Planning is the perfect course for those who want to start a career as a wedding planner. It is a fast paced course that can be completed in 12 weeks and covers all elements of planning a wedding as outlined in the units below. Students on this course have often planned their own wedding and are looking to take their love of weddings to a new level and learn the tricks of the trade. Upon completion of the course you will receive a certificate which is bench marked at a Level 3 NVQ and be able to use the title of Qualified Wedding Organiser which is recognised internationally.</p>
      <nav class="course-actions"><a href="#">read more</a><a href="#">enquire</a><a href="#">enrol online</a></nav>
    </div>
  </article>

  <article class="course" style="left:444px">
    <svg class="course-icon" viewBox="0 0 78 46" aria-hidden="true"><polygon points="39,2 76,16 39,30 2,16" fill="#1a1412"/><path d="M18 22 v14 c10 8 32 8 42 0 v-14 l-21 8z" fill="#1a1412"/><path d="M68 19 v16" stroke="#1a1412" stroke-width="2"/><rect x="65.5" y="34" width="5" height="9" fill="#1a1412"/></svg>
    <h2 class="course-title">Certificate in<br>Event Planning</h2>
    <p class="course-price">Get started for as little as £70</p>
    <div class="course-body">
      <p>The Certificate in Event Planning is the perfect course for those who want to start a career as an event planner. It is a fast paced course that can be completed in 12 weeks and covers all elements of planning an event as outlined in the units below. Students on this course are usually looking to plan festivals, pop-up events, product launches, conferences, trade shows, award nights and a multitude of corporate events.<br>Upon completion of the course you will receive a certificate which is bench marked at a Level 3 NVQ and be able to use the title of Qualified Event Practitioner which is recognised internationally.</p>
      <nav class="course-actions"><a href="#">read more</a><a href="#">enquire</a><a href="#">enrol online</a></nav>
    </div>
  </article>

  <article class="course" style="left:797px">
    <svg class="course-icon" viewBox="0 0 78 46" aria-hidden="true"><polygon points="39,2 76,16 39,30 2,16" fill="#1a1412"/><path d="M18 22 v14 c10 8 32 8 42 0 v-14 l-21 8z" fill="#1a1412"/><path d="M68 19 v16" stroke="#1a1412" stroke-width="2"/><rect x="65.5" y="34" width="5" height="9" fill="#1a1412"/></svg>
    <h2 class="course-title">Certificate in<br>Event Design</h2>
    <p class="course-price">Get started for as little as £75</p>
    <div class="course-body">
      <p>The Certificate in Event Design is the perfect course for those who want to add design to their existing skills. It is a fast paced course that can be completed in 12 weeks and covers all elements of designing an event as outlined in the units below. Students on this course typically have experience in either wedding or event planning and want to learn the design aspect so they can give their client a full experience. It allows them to not only plan the elements but design the overall concept using tools such as inspiration boards, design software and much more. Upon completion of the course you will receive a certificate which is bench marked at a Level 4 NVQ and be able to use the title of Qualified Event Stylist which is recognised internationally.</p>
      <nav class="course-actions"><a href="#">read more</a><a href="#">enquire</a><a href="#">enrol online</a></nav>
    </div>
  </article>

  <footer class="contact-bar">
    <div class="contact-item" style="left:408px">
      <svg viewBox="0 0 17 17" aria-hidden="true"><circle cx="8.5" cy="8.5" r="8.5" fill="#fff"/><rect x="4" y="5.5" width="9" height="6" fill="none" stroke="#f3876d" stroke-width="1.2"/><path d="M4 5.8 l4.5 3.4 l4.5 -3.4" fill="none" stroke="#f3876d" stroke-width="1.2"/></svg>
      mia@harbourevents.co.uk
    </div>
    <div class="contact-item" style="left:622px">
      <svg viewBox="0 0 17 17" aria-hidden="true"><circle cx="8.5" cy="8.5" r="8.5" fill="#fff"/><path d="M5.5 4.5 l1.8 0 l0.8 2.2 l-1.1 0.9 c0.6 1.3 1.5 2.2 2.7 2.8 l0.9 -1.1 l2.2 0.8 l0 1.8 c-4 0.4 -7.6 -3.2 -7.3 -7.4z" fill="#f3876d"/></svg>
      0845 270 4418.
    </div>
    <div class="contact-item" style="left:835px">
      <svg viewBox="0 0 17 17" aria-hidden="true"><circle cx="8.5" cy="8.5" r="8.5" fill="#fff"/><circle cx="8.5" cy="8.2" r="4" fill="none" stroke="#f3876d" stroke-width="1.2"/><path d="M5.8 11 l-1.3 2 l2.4 -0.9" fill="#f3876d"/></svg>
    </div>
  </footer>
</main>
</body>
</html>
```